Ceiling fan flyer design

We are after a double sided flyer design offering ceiling fan installations

Target Market(s)

Home owners

Requirements
Must have
• content listed

```html
<!DOCTYPE html>
<html lang="en">
<head>
<meta charset="utf-8">
<title>Ceiling Fan Flyer – Breezeway Electrical</title>
<link href="https://fonts.googleapis.com/css2?family=Roboto+Condensed:wght@700&family=Source+Sans+3:wght@300;400;600;700&display=swap" rel="stylesheet">
<style>
:root{
  --stage:#e9ebee;
  --blue-deep:#123c94;
  --blue-mid:#1d67c4;
  --blue-bright:#2a97e0;
  --red:#c41f28;
  --orange:#f08a1c;
  --white:#ffffff;
  --ink-blue:#2a3a8f;
  --ink-dark:#333a44;
  --pale:#dcecf8;
  --pale-edge:#b9d6ee;
}
*{box-sizing:border-box;margin:0;padding:0}
html,body{width:1200px;height:1155px;overflow:hidden;background:var(--stage)}
body{position:relative;font-family:"Source Sans 3",sans-serif}
.flyer{position:absolute;top:88px;width:475px;height:980px;overflow:hidden;box-shadow:0 4px 14px rgba(0,0,0,.18)}
.flyer--front{left:90px;background:linear-gradient(100deg,var(--blue-bright) 0%,var(--blue-mid) 55%,var(--blue-deep) 100%)}
.flyer--back{left:635px;background:radial-gradient(ellipse at 50% 45%,var(--white) 0%,var(--pale) 60%,var(--pale-edge) 100%)}
.abs{position:absolute}
.center{left:0;right:0;text-align:center}

/* front */
.mascot{left:110px;top:20px;width:300px;height:225px;border-radius:40px;background:radial-gradient(circle at 60% 45%,rgba(255,255,255,.45),rgba(60,160,90,.35) 55%,rgba(255,255,255,0) 75%)}
.brand{left:96px;top:256px;width:240px;font-weight:700;font-size:22px;line-height:1.1;color:var(--orange);text-transform:uppercase}
.headline{font-family:"Roboto Condensed",sans-serif;font-weight:700;color:var(--white);font-size:58px;line-height:1;text-shadow:0 2px 4px rgba(0,0,0,.35)}
.sub{top:492px;font-weight:600;font-size:33px;color:var(--white)}
.lead{top:546px;padding:0 50px;font-weight:600;font-size:18.5px;line-height:1.2;color:var(--white)}
.fan-photo{left:40px;top:625px;width:390px;height:200px;border-radius:50%;background:radial-gradient(ellipse at 50% 45%,#c9b98d 0%,#5a4c38 35%,rgba(40,34,28,.6) 60%,rgba(40,34,28,0) 75%)}
.offer-band{left:0;top:820px;width:475px;height:160px}
.offer{left:50px;top:864px;font-family:"Roboto Condensed",sans-serif;font-weight:700;font-size:36px;line-height:1.2;color:var(--white)}

/* back */
.install-photo{left:0;top:0;width:475px;height:240px}
.section-title{left:36px;top:198px;font-weight:600;font-size:24px;color:var(--ink-blue)}
.promises{left:36px;top:238px;width:410px;list-style:none}
.promises li{position:relative;padding-left:28px;font-size:15.5px;line-height:1.2;color:var(--ink-dark);margin-bottom:5px}
.promises svg{position:absolute;left:0;top:2px;width:15px;height:15px}
.testimonials-title{top:476px;font-size:21px;color:var(--red);font-weight:400}
.testimonials{left:44px;top:506px;width:390px;height:158px;border-radius:12px;background:linear-gradient(180deg,#3a86d6 0%,#1a56b4 100%);box-shadow:0 4px 8px rgba(0,0,0,.25);padding:12px 20px;color:var(--white)}
.quote{font-size:14.5px;line-height:1.25}
.quote-by{text-align:right;font-weight:600;font-size:14.5px;margin:4px 0 16px}
.conditions-title{top:684px;font-weight:700;font-size:20px;color:var(--ink-blue)}
.conditions{top:714px;font-weight:600;font-size:14px;line-height:1.35;color:var(--ink-blue)}
.contact-label{top:784px;font-weight:300;font-size:22px;color:var(--ink-dark)}
.phone{top:810px;font-family:"Roboto Condensed",sans-serif;font-weight:700;font-size:44px;letter-spacing:3px;color:var(--ink-dark)}
.cards{top:873px;display:flex;justify-content:center;gap:6px}
.card{width:70px;height:44px;border-radius:3px;border:2px solid var(--white);box-shadow:0 1px 3px rgba(0,0,0,.3)}
.card--a{background:#1a2b7a}.card--b{background:#2a2a2a}.card--c{background:#2b7ec4}
.web{top:930px;font-weight:700;font-size:23px;letter-spacing:1px;color:var(--ink-blue)}
</style>
</head>
<body>

<section class="flyer flyer--front">
  <div class="abs mascot" role="img" aria-label="Cartoon superhero electrician mascot holding up a light bulb"></div>
  <div class="abs brand">Breezeway Electrical Pty Ltd</div>
  <h1 class="abs center headline" style="top:335px">Hot sweaty</h1>
  <p class="abs center headline" style="top:408px">Uncomfortable</p>
  <h2 class="abs center sub">A breeze without the cost!</h2>
  <p class="abs center lead">Enjoy the gentle breeze &amp; cooling effect of a ceiling fan to help you sleep soundly at night &amp; be more productive during the day.</p>
  <div class="abs fan-photo" role="img" aria-label="Photo of a five-blade ceiling fan"></div>
  <svg class="abs offer-band" viewBox="0 0 475 160" preserveAspectRatio="none">
    <path d="M0 14 C150 -2 330 10 475 60 L475 160 L0 160 Z" fill="var(--white)"/>
    <path d="M0 24 C150 8 330 22 475 78 L475 160 L0 160 Z" fill="var(--red)"/>
  </svg>
  <p class="abs offer">Save $25 OFF every<br>2nd fan installed</p>
</section>

<section class="flyer flyer--back">
  <svg class="abs install-photo" viewBox="0 0 475 240" role="img" aria-label="Photo of hands installing a ceiling fan">
    <defs>
      <linearGradient id="photoTone" x1="0" y1="0" x2="1" y2="1">
        <stop offset="0" stop-color="#7a5238"/>
        <stop offset=".45" stop-color="#b48a6a"/>
        <stop offset="1" stop-color="#e7ddd0"/>
      </linearGradient>
    </defs>
    <path d="M0 0 H475 V190 C330 200 150 150 0 90 Z" fill="url(#photoTone)"/>
    <path d="M0 90 C150 150 330 200 475 190 V218 C330 220 150 175 0 100 Z" fill="var(--red)"/>
  </svg>
  <h2 class="abs section-title">We guarantee to:</h2>
  <ul class="abs promises">
    <li><svg viewBox="0 0 16 16"><circle cx="8" cy="8" r="7" fill="var(--red)"/><path d="M4.5 8.2l2.3 2.3 4.7-5" stroke="#fff" stroke-width="2" fill="none"/></svg>Always be on time, or we pay you $100</li>
    <li><svg viewBox="0 0 16 16"><circle cx="8" cy="8" r="7" fill="var(--red)"/><path d="M4.5 8.2l2.3 2.3 4.7-5" stroke="#fff" stroke-width="2" fill="none"/></svg>Tell you the exact cost before any job begins</li>
    <li><svg viewBox="0 0 16 16"><circle cx="8" cy="8" r="7" fill="var(--red)"/><path d="M4.5 8.2l2.3 2.3 4.7-5" stroke="#fff" stroke-width="2" fill="none"/></svg>Provide you with a fixed price guarantee, assuring you have no extra costs</li>
    <li><svg viewBox="0 0 16 16"><circle cx="8" cy="8" r="7" fill="var(--red)"/><path d="M4.5 8.2l2.3 2.3 4.7-5" stroke="#fff" stroke-width="2" fill="none"/></svg>Leave your place as clean as it was when we first arrived</li>
    <li><svg viewBox="0 0 16 16"><circle cx="8" cy="8" r="7" fill="var(--red)"/><path d="M4.5 8.2l2.3 2.3 4.7-5" stroke="#fff" stroke-width="2" fill="none"/></svg>Return, and fix it for free, if its not right</li>
    <li><svg viewBox="0 0 16 16"><circle cx="8" cy="8" r="7" fill="var(--red)"/><path d="M4.5 8.2l2.3 2.3 4.7-5" stroke="#fff" stroke-width="2" fill="none"/></svg>Return your telephone calls promptly</li>
    <li><svg viewBox="0 0 16 16"><circle cx="8" cy="8" r="7" fill="var(--red)"/><path d="M4.5 8.2l2.3 2.3 4.7-5" stroke="#fff" stroke-width="2" fill="none"/></svg>Provide a minimum 12 Month warranty on all parts</li>
    <li><svg viewBox="0 0 16 16"><circle cx="8" cy="8" r="7" fill="var(--red)"/><path d="M4.5 8.2l2.3 2.3 4.7-5" stroke="#fff" stroke-width="2" fill="none"/></svg>Provide friendly, helpful service and advice</li>
  </ul>
  <h3 class="abs center testimonials-title">TESTIMONIALS</h3>
  <div class="abs testimonials">
    <p class="quote">“We can now sleep! Wowwhat a difference! Thanks Daniel for your help.”</p>
    <p class="quote-by">Marcus &amp; Leah Thornbury</p>
    <p class="quote">“Super service! What apleasant change. Daniel could not have done moreto ensure our satisfaction..”</p>
    <p class="quote-by" style="margin-bottom:0">Sam &amp; Rosa, Ashfield</p>
  </div>
  <h3 class="abs center conditions-title">CONDITIONS:</h3>
  <p class="abs center conditions">Mention this ad when booking to receive offer.<br>Limit one per household. Cannot be combined with any other offer.</p>
  <p class="abs center contact-label">CONTACT US</p>
  <p class="abs center phone">1300 482 716</p>
  <div class="abs center cards">
    <span class="card card--a"></span><span class="card card--b"></span><span class="card card--c"></span>
  </div>
  <p class="abs center web">www.breezewayelectrical.com.au</p>
</section>

</body>
</html>
```